Consultancy Business Card Design

We need a business card design for a new company based in singapore called FortyOne. FortyOne a boutique consultancy firm offering broad-based business solutions, from conception to re-invention, for ventures from new start-ups to long-running traditional businesses.
Its 2 main divisions (Food & Beverage Operations and Construction & Project Management) have access to a wide range of networks, knowledge bases, and resources to service its clients across numerous diverse sectors. This includes, and is not limited to, construction, F&B, and retail.
We are a company that combines the ambition, boldness and energy of one in the 20s with the dedication, level-headedness and dependability of one entering its 30s. Bridging the experiences of the old with ideals of the young, we draw on the positives of both to create a unique synergy.
We hope to see designs that fits our company profile.
Boutique
FortyOne(Company Name)
Marcus Leow (Name)
Principle Consultant (Title)
F&B and Hospitality (Division)
(+65) 8364 5170 (Contact no.)
marcus@fortyone-example.com.sg (Email)

```html
<!DOCTYPE html>
<html lang="en">
<head>
<meta charset="utf-8">
<title>FortyOne Business Card</title>
<link rel="stylesheet" href="https://fonts.googleapis.com/css2?family=Quicksand:wght@400;500;700&display=swap">
<style>
  :root {
    --backdrop: #e7e4e0;
    --card: #1b1b1b;
    --accent: #4db3e6;
    --muted: #3a3a3a;
    --faint: #232323;
    --mark-dark: #333333;
    --ink: #111111;
  }
  * { box-sizing: border-box; margin: 0; padding: 0; }
  html, body {
    width: 1200px; height: 790px; overflow: hidden;
    background: var(--backdrop);
    font-family: "Quicksand", sans-serif;
  }
  .canvas { position: relative; width: 1200px; height: 790px; }

  .card {
    position: absolute; top: 202px;
    width: 465px; height: 292px;
    background: var(--card);
    border-radius: 12px;
    overflow: hidden;
  }
  .card--front { left: 107px; }
  .card--back { left: 638px; }

  /* Front: brand lockup */
  .lockup {
    position: absolute; left: 133px; top: 92px;
    display: flex; align-items: flex-end; gap: 6px;
  }
  .lockup__dot {
    width: 97px; height: 97px; border-radius: 50%;
    background: var(--accent);
  }
  .lockup__name {
    color: var(--accent); font-size: 15px; font-weight: 500;
    letter-spacing: 1.5px; line-height: 1; margin-bottom: 2px;
  }

  /* Back: details */
  .back__halo {
    position: absolute; left: 250px; top: -40px;
    width: 250px; height: 250px; border-radius: 50%;
    background: var(--faint);
  }
  .identity { position: absolute; left: 48px; top: 96px; width: 180px; }
  .identity__company {
    color: var(--accent); font-size: 11px; letter-spacing: 1px; line-height: 1;
  }
  .identity__name {
    color: var(--accent); font-size: 20px; letter-spacing: 1.5px;
    line-height: 1; margin-top: 4px; white-space: nowrap;
  }
  .identity__name strong { font-weight: 700; }
  .identity__title {
    color: var(--accent); font-size: 9.5px; letter-spacing: 1px;
    text-align: right; margin-top: 5px; white-space: nowrap;
  }
  .contact {
    position: absolute; left: 31px; top: 210px;
    list-style: none; color: var(--muted);
    font-size: 11px; letter-spacing: 1.2px; line-height: 12.5px;
  }

  /* Mark variants */
  .badge {
    position: absolute; top: 525px;
    width: 234px; height: 234px; border-radius: 50%;
    display: flex; align-items: center; justify-content: center;
    color: var(--ink); font-size: 34px; font-weight: 500; letter-spacing: 1px;
  }
  .badge--accent { left: 218px; background: var(--accent); }
  .badge--dark { left: 761px; background: var(--mark-dark); }
</style>
</head>
<body>
<main class="canvas">
  <section class="card card--front" aria-label="Card front">
    <div class="lockup">
      <span class="lockup__dot"></span>
      <span class="lockup__name">fortyone</span>
    </div>
  </section>

  <section class="card card--back" aria-label="Card back">
    <span class="back__halo"></span>
    <div class="identity">
      <p class="identity__company">FortyOne</p>
      <p class="identity__name">Marcus <strong>Leow</strong></p>
      <p class="identity__title">Principle Consultant</p>
    </div>
    <ul class="contact">
      <li>Division: F&amp;B and Hospitality</li>
      <li>Phone: (+65) 8364 5170</li>
      <li>Email: marcus@fortyone-example.com.sg</li>
    </ul>
  </section>

  <div class="badge badge--accent">fortyone</div>
  <div class="badge badge--dark">fortyone</div>
</main>
</body>
</html>
```